Five Quill Voices, "Drafting and Polishing Made Bright"

We need a brochure that provides background about our company, identifies our products and services and provides our contact information. If possible, We would like the designer to use an Office suite product such as Word or Publisher to create the brochure if possible. We would like photos, color, something that inspires customers to use our services. We have attached a copy of a draft brochure and we believe the text in the brochure is good, but the brochure is cold, bland and lacks color, style and a fresh quality. We would like all text in the brochure to be included as well as the attached logo and company name somewhere on the front and back of the brochure. Please feel free to resize the logo and use creative license to develop the brochure as you please. However, the brochure colors should compliment the dark blue, light blue and black colors in the logo. Most of all, the brochure needs to be engaging, inviting, fresh and ultra professional. Thanks!

Target Market(s)

Small and large scale businesses who would use self-help books, writing services for blogs and Social Page posts, newsletters and manuscript reviews.

Industry/Entity Type

Marketing

Font styles to use
Serif

Colors
0655a3
3377b5
85acd3
000000

Requirements
Must have
• -Logo and company name; text in draft brochure
• -Color and business photos which relate to the products/services provided
• -Inspiring, engaging, professional feel and style
• -I would like colors which compliment the logo colors (perhaps the colors below, but we are open to designer choices
• -Since this is a writing/editing business, something in the brochure that reflects that would be good.
Nice to have
• -Open; depends on the designer preference
• -Use of Office Word or Publisher program, but we are open to the use of other programs.
Should not have
• -Bland brochure with only text

```html
<!DOCTYPE html>
<html lang="en">
<head>
<meta charset="utf-8">
<title>Five Quill Voices – Brochure Inside Spread</title>
<link rel="stylesheet" href="https://fonts.googleapis.com/css2?family=Crimson+Pro:wght@400;600&display=swap">
<style>
  :root {
    --navy: #0655a3;
    --mid-blue: #3377b5;
    --light-blue: #85acd3;
    --ink: #000000;
    --body-ink: #2b2b2b;
    --mist: #e6e7e9;
    --paper: #ffffff;
    --fold: #d9dde3;
  }
  * { box-sizing: border-box; margin: 0; padding: 0; }
  html, body { width: 1200px; height: 956px; overflow: hidden; background: var(--paper); }
  body { font-family: "Crimson Pro", Georgia, serif; color: var(--body-ink); }

  .spread { position: relative; width: 1200px; height: 956px; display: flex; }
  .spread-art { position: absolute; inset: 0; pointer-events: none; }

  .panel { position: relative; width: 400px; height: 956px; padding: 0 40px; z-index: 1; }
  .panel + .panel { border-left: 1px solid var(--fold); }

  .section-title {
    font-weight: 400; font-size: 27px; line-height: 1.15; letter-spacing: 0.5px;
    color: var(--navy); text-transform: uppercase; margin-bottom: 18px;
  }
  .sub-title { font-weight: 600; font-size: 18px; color: var(--mid-blue); margin: 14px 0 6px; }
  p { font-size: 15.5px; line-height: 1.42; margin-bottom: 12px; }

  .overview { padding-top: 64px; }

  .values { list-style: none; margin-top: 22px; }
  .values li { display: flex; align-items: center; gap: 14px; margin-bottom: 16px; font-size: 14.5px; line-height: 1.35; }
  .value-icon { flex: 0 0 38px; width: 38px; height: 38px; }

  .services { padding-top: 226px; }
  .details { padding-top: 244px; }

  .petal-art {
    position: absolute; left: 0; right: 0; bottom: 0; height: 104px; z-index: 0;
    background: linear-gradient(to bottom, rgba(133,172,211,0) 0%, rgba(133,172,211,0.55) 55%, rgba(6,85,163,0.55) 100%);
  }
  .services > * { position: relative; z-index: 1; }
  .services > .petal-art { position: absolute; z-index: 0; }
  .services > .photo-pair { position: absolute; }
</style>
</head>
<body>
<main class="spread">
  <svg class="spread-art" width="1200" height="956" viewBox="0 0 1200 956" aria-hidden="true">
    <path d="M0 0 H230 C170 20 90 22 0 70 Z" fill="var(--mist)"/>
    <path d="M400 0 H1200 V95 C1080 60 980 160 860 150 C760 140 700 70 560 110 C480 132 430 120 400 100 Z" fill="var(--mist)"/>
  </svg>

  <section class="panel overview">
    <h2 class="section-title">Company Overview<br>Description</h2>
    <p>Five Quill Voices Publications dba Five Quill Voices was founded in 2008 by Marian T. Holloway, a Social Services Administrator, author and publisher. Five Quill Voices has become a trusted name with a solid local reputation as a small business that offers non-fiction books which focus on improving the financial and physical health of adults. Five Quill Voices also provides a multi-disciplinary approach to editing and writing services related to trending topics, educational, evergreen pieces or social media matters.</p>
    <p>Since early 2008, Five Quill Voices' operations have focused on producing scalable, high-quality content solutions to meet unique business needs to develop content to engage audiences. At Five Quill Voices, we implemented sound, organizational goals which center around our values:</p>
    <ul class="values">
      <li><svg class="value-icon" viewBox="0 0 38 38" aria-hidden="true"><circle cx="19" cy="19" r="18" fill="var(--mid-blue)"/><path d="M11 19 l6 6 l10 -12" fill="none" stroke="#fff" stroke-width="3" stroke-linecap="round"/></svg>Easy order interface complimented by excellent customer service levels.</li>
      <li><svg class="value-icon" viewBox="0 0 38 38" aria-hidden="true"><circle cx="19" cy="19" r="18" fill="var(--mid-blue)"/><path d="M11 19 l6 6 l10 -12" fill="none" stroke="#fff" stroke-width="3" stroke-linecap="round"/></svg>Qualified writers who provide expert editing and writing services.</li>
      <li><svg class="value-icon" viewBox="0 0 38 38" aria-hidden="true"><circle cx="19" cy="19" r="18" fill="var(--mid-blue)"/><path d="M11 19 l6 6 l10 -12" fill="none" stroke="#fff" stroke-width="3" stroke-linecap="round"/></svg>Engagement of targeted audiences designed to increase sales and enhance client work product.</li>
      <li><svg class="value-icon" viewBox="0 0 38 38" aria-hidden="true"><circle cx="19" cy="19" r="18" fill="var(--mid-blue)"/><path d="M11 19 l6 6 l10 -12" fill="none" stroke="#fff" stroke-width="3" stroke-linecap="round"/></svg>Timely deliverables with 100% satisfaction.</li>
    </ul>
  </section>

  <section class="panel services">
    <div class="petal-art" role="img" aria-label="Decorative blue lotus petal illustration"></div>
    <svg class="photo-pair" style="left:60px;top:18px" width="300" height="180" viewBox="0 0 300 180" role="img" aria-label="Photos of hands typing on a laptop keyboard">
      <defs><linearGradient id="photoA" x1="0" y1="0" x2="1" y2="1"><stop offset="0" stop-color="#cfd8e2"/><stop offset="1" stop-color="#5d6f84"/></linearGradient></defs>
      <circle cx="95" cy="85" r="80" fill="url(#photoA)" stroke="#fff" stroke-width="5"/>
      <circle cx="225" cy="70" r="58" fill="url(#photoA)" stroke="#fff" stroke-width="5"/>
    </svg>
    <h2 class="section-title">Products &amp; Services</h2>
    <p>Five Quill Voices offers a highly-focused service approach to provide non-fiction books and offer quality editing and writing services to produce blog and Social Page posts, white papers, newsletters and manuscript reviews.</p>
    <h3 class="sub-title">Non-fiction books</h3>
    <p>We are developing a series of books that will aid Baby Boomers and the Generation X population to develop and maintain good, financial planning practices and maintain stable emotional and physical health while aging. The first book in the series, Growing Older Wisely will be released in the Summer of 2016. Growing Older Wisely is a step-by-step guide to aging in America which includes estate planning, wills and trusts, caregiving, senior housing, and coping with the loss of a loved one.</p>
    <h3 class="sub-title">Blog and Social Page Post</h3>
    <p>Blog posts are used to increase brand awareness in search engines and attract new website visitors with relevant, valuable content.</p>
    <p>With client guidance, writers begin by mapping out each blog post to ensure topics, titles, keywords and formatting</p>
  </section>

  <section class="panel details">
    <svg style="position:absolute;left:90px;top:8px" width="220" height="210" viewBox="0 0 220 210" role="img" aria-label="Photo of a person writing at a laptop">
      <defs><linearGradient id="photoB" x1="0" y1="0" x2="1" y2="1"><stop offset="0" stop-color="#e3e7ec"/><stop offset="1" stop-color="#6b7a8c"/></linearGradient></defs>
      <circle cx="110" cy="105" r="98" fill="url(#photoB)" stroke="#fff" stroke-width="6"/>
    </svg>
    <p>engaging targeted audiences and support your business commercial goals.</p>
    <p>A standard blog post (which is 500 to 650 words) may be designed to devote special attention to a topic. Blog posts are short but are still detailed enough to be mobile- and reader-friendly. Further, standard blog posts with navigational aids such as numbered lists, bullet points and headers, can be informative and engaging.</p>
    <h3 class="sub-title">White Papers</h3>
    <p>White papers are essential to establishing a brand as a trustworthy leader in a specific industry. These high-quality content pieces build credibility among online audiences by demonstrating expertise and offering good lead generation opportunities through downloads from potential customers. Five Quill Voices will work with you to determine the topics that resonate most with your target audience to develop valuable, relevant content that supports business goals.</p>
  </section>
</main>
</body>
</html>
```